Sports hypnotherapist needs electronic letterhead design

Need a simple but classy design for a letterhead that looks good when printed. Its for a hypnotherapist who specialises in elite sport. Should have my company name and address and website details on it. I specialise in footballers.
Should look good electronically and when printed.
Include all contact details as shown in the must haves.

Target Market(s)

Sports people, elite sport.

Industry/Entity Type

Hypnotherapy

Font styles to use
Sans Serif

Colors

Designer to choose colors to be used in the design.

Requirements
Must have
• NEEDS TO BE DESIGNED IN MS WORD
• Logo +
• Tidewell Path Hypnotherapists
• 27 Marlowby Close
• Bracknell
• RG14 3TX
• Tel: 07814 265173
• E: tidewellcoaching@brookmail.example
• www: http://www.tidewell-path.example.
• Colin Dearsley
• Clinical hypnotherapist, hypnoanalyst, mental resilience coach, MSc, Dip PHH
Nice to have
• A watermark?
• Plenty of space for the A4 letter
• Prints well.
Should not have
• Too much clutter.
• Too much colour that will be costly to print.

```html
<!DOCTYPE html>
<html lang="en">
<head>
<meta charset="utf-8">
<title>Tidewell Path Letterhead</title>
<link href="https://fonts.googleapis.com/css2?family=Open+Sans:wght@400;600;700&display=swap" rel="stylesheet">
<style>
  :root {
    --backdrop: #d6d6d8;
    --paper: #fdfdfd;
    --ink: #1a1a1a;
    --accent: #29abe2;
    --watermark-grey: #dcdcde;
    --watermark-blue: #eef5fa;
  }
  * { margin: 0; padding: 0; box-sizing: border-box; }
  html, body {
    width: 1200px; height: 900px; overflow: hidden;
    background: var(--backdrop);
    font-family: "Open Sans", sans-serif;
    color: var(--ink);
  }
  .letterhead {
    position: absolute; left: 296px; top: 57px;
    width: 606px; height: 785px;
    background: var(--paper);
    overflow: hidden;
  }
  .brand-name {
    position: absolute; left: 62px; top: 58px;
    font-size: 27px; font-weight: 700; line-height: 1; letter-spacing: -0.3px;
    color: var(--ink);
  }
  .practitioner {
    position: absolute; left: 439px; top: 35px;
    border-left: 2px solid var(--accent);
    padding-left: 8px; height: 73px;
  }
  .practitioner-name {
    font-size: 15px; font-weight: 600; color: var(--accent); line-height: 1.2; margin-top: 3px;
  }
  .practitioner-credentials {
    font-size: 8.5px; font-weight: 600; line-height: 1.2; margin-top: 1px;
  }
  .watermark {
    position: absolute; left: 262px; top: 280px;
    width: 344px; height: 505px;
    border-radius: 60px 60px 0 0;
    background: linear-gradient(100deg, var(--watermark-grey) 0%, var(--watermark-grey) 45%, var(--watermark-blue) 75%, rgba(238,245,250,0) 100%);
    opacity: 0.9;
  }
  .contact {
    position: absolute; left: 63px; top: 701px;
    font-size: 8.5px; line-height: 1.2;
  }
  .contact-company { color: var(--accent); }
  .contact-address { font-weight: 600; margin-bottom: 6px; }
  .contact-line { display: flex; align-items: center; gap: 5px; height: 11px; font-weight: 600; }
  .contact-line svg { width: 8px; height: 8px; fill: var(--accent); flex: none; }
</style>
</head>
<body>
  <main class="letterhead">
    <div class="brand-name">Tidewell Path</div>

    <div class="practitioner">
      <p class="practitioner-name">Colin Dearsley</p>
      <p class="practitioner-credentials">Clinical hypnotherapist,<br>Hypnoanalyst,<br>Mental Resilience Coach,<br>MSc, Dip PHH</p>
    </div>

    <div class="watermark" role="img" aria-label="Faint watermark of the practice emblem"></div>

    <address class="contact" style="font-style:normal">
      <p class="contact-company">Tidewell Path Hypnotherapists</p>
      <p class="contact-address">27 Marlowby Close, Bracknell&nbsp; RG14 3TX</p>
      <p class="contact-line">
        <svg viewBox="0 0 8 8" aria-hidden="true"><rect width="8" height="8" rx="1"/><path d="M2.2 1.6c.3 2.2 1.8 3.8 4 4.4l-.6.7C3.4 6.3 1.6 4.5 1.4 2.2z" fill="#fff"/></svg>
        07814 265173
      </p>
      <p class="contact-line">
        <svg viewBox="0 0 8 8" aria-hidden="true"><rect y="1.5" width="8" height="5" rx="0.5"/><path d="M0.4 1.9 4 4.6 7.6 1.9" stroke="#fff" stroke-width="0.7" fill="none"/></svg>
        tidewellcoaching@brookmail.example
      </p>
      <p class="contact-line">
        <svg viewBox="0 0 8 8" aria-hidden="true"><circle cx="4" cy="4" r="3.6" fill="none" stroke="var(--accent)" stroke-width="0.8"/><ellipse cx="4" cy="4" rx="1.5" ry="3.6" fill="none" stroke="var(--accent)" stroke-width="0.6"/><path d="M0.4 4h7.2" stroke="var(--accent)" stroke-width="0.6"/></svg>
        www.tidewell-path.example
      </p>
    </address>
  </main>
</body>
</html>
```